International Trading Company, 'KIRO' needs a Business Card

The company name is "KIRO" and it has own logo design.
I'd like to use its logo on this business card.
I need two side Business Card.
I'll look forward to your great design.
Thank you very much in advance.

Contact Information for Business Card

Company Name : Kiro Harbour Limited
Information Example
Dorian Pallister
Mobile(use icon please) : 1 (212) 555-0143
Tel(use icon please) : 1 (212) 555-0178
Email(use icon please) : dorian27@kiroharbour-mail.com
Address(use icon please) : 482 Halden Ave, New York, NY 10160, USA

```html
<!DOCTYPE html>
<html lang="en">
<head>
<meta charset="utf-8">
<title>Kiro Harbour Limited — Business Card</title>
<link rel="stylesheet" href="https://fonts.googleapis.com/css2?family=Roboto:wght@400;500;700&display=swap">
<style>
  :root {
    --canvas-bg: #e4e2df;
    --card-black: #0c0c0c;
    --card-grey: #5f5f5f;
    --logo-grey-front: #6b6b6b;
    --logo-grey-back: #5c5c5c;
    --ink-dark: #141414;
    --shadow: rgba(0, 0, 0, 0.22);
  }
  * { box-sizing: border-box; margin: 0; padding: 0; }
  html, body {
    width: 1200px; height: 1200px; overflow: hidden;
    background: var(--canvas-bg);
    font-family: "Roboto", Arial, sans-serif;
  }
  .canvas {
    width: 1200px; height: 1200px;
    display: flex; flex-direction: column;
    align-items: center; justify-content: center; gap: 60px;
  }
  .card {
    position: relative;
    width: 910px; height: 520px;
    overflow: hidden;
    box-shadow: 0 10px 28px var(--shadow);
  }

  /* Front */
  .card--front { background: var(--card-black); }
  .brand {
    position: absolute;
    display: flex; flex-direction: column; align-items: flex-end;
    font-weight: 700; line-height: 1;
  }
  .brand__name { letter-spacing: 0.02em; }
  .brand__sub { letter-spacing: 0.06em; }
  .card--front .brand {
    left: 0; right: 0; top: 118px;
    align-items: center;
    color: var(--logo-grey-front);
  }
  .card--front .brand__name { font-size: 150px; }
  .card--front .brand__sub { font-size: 34px; margin-top: 6px; }
  .website {
    position: absolute; left: 0; right: 0; top: 383px;
    text-align: center;
    color: var(--logo-grey-front);
    font-size: 20px; font-weight: 500; letter-spacing: 0.32em;
  }
  .front-stripe {
    position: absolute; left: 0; right: 0; top: 428px; height: 42px;
    background: var(--card-grey);
  }

  /* Back */
  .card--back { background: var(--card-grey); }
  .back-band {
    position: absolute; left: 0; right: 0; top: 0; height: 236px;
    background: var(--card-black);
  }
  .card--back .brand {
    left: 120px; top: 48px; align-items: flex-start;
    color: var(--logo-grey-back);
  }
  .card--back .brand__name { font-size: 120px; }
  .card--back .brand__sub { font-size: 27px; margin-top: 6px; }
  .holder-name {
    position: absolute; left: 46px; top: 262px;
    color: var(--ink-dark);
    font-size: 36px; font-weight: 700; letter-spacing: 0.01em;
  }
  .contact-list {
    position: absolute; left: 560px; top: 268px;
    list-style: none;
    display: flex; flex-direction: column; gap: 14px;
  }
  .contact-item {
    display: flex; align-items: center; gap: 14px;
    color: var(--ink-dark);
    font-size: 18px; font-weight: 400;
  }
  .contact-item svg { width: 20px; height: 20px; flex: none; fill: var(--ink-dark); }
  .address {
    position: absolute; left: 46px; top: 440px;
  }
</style>
</head>
<body>
<main class="canvas">

  <section class="card card--front" aria-label="Business card front">
    <div class="brand">
      <span class="brand__name">KIRO</span>
      <span class="brand__sub">HARBOUR LIMITED</span>
    </div>
    <p class="website">www.kiroharbour.com</p>
    <div class="front-stripe"></div>
  </section>

  <section class="card card--back" aria-label="Business card back">
    <div class="back-band"></div>
    <div class="brand">
      <span class="brand__name">KIRO</span>
      <span class="brand__sub">HARBOUR LIMITED</span>
    </div>

    <h1 class="holder-name">Dorian Pallister</h1>

    <ul class="contact-list">
      <li class="contact-item">
        <svg viewBox="0 0 24 24" aria-hidden="true"><path d="M7 1h10a2 2 0 0 1 2 2v18a2 2 0 0 1-2 2H7a2 2 0 0 1-2-2V3a2 2 0 0 1 2-2zm0 3v14h10V4H7zm5 15.2a1.2 1.2 0 1 0 0 2.4 1.2 1.2 0 0 0 0-2.4z"/></svg>
        <span>1 (212) 555-0143</span>
      </li>
      <li class="contact-item">
        <svg viewBox="0 0 24 24" aria-hidden="true"><path d="M6.6 10.8a15.1 15.1 0 0 0 6.6 6.6l2.2-2.2a1 1 0 0 1 1-.25 11.4 11.4 0 0 0 3.6.57 1 1 0 0 1 1 1V20a1 1 0 0 1-1 1A17 17 0 0 1 3 4a1 1 0 0 1 1-1h3.5a1 1 0 0 1 1 1c0 1.25.2 2.45.57 3.57a1 1 0 0 1-.25 1z"/></svg>
        <span>1 (212) 555-0178</span>
      </li>
      <li class="contact-item">
        <svg viewBox="0 0 24 24" aria-hidden="true"><path d="M2 4h20v16H2V4zm2 2v.5l8 5.5 8-5.5V6H4zm16 2.9-8 5.5-8-5.5V18h16V8.9z"/></svg>
        <span>dorian27@kiroharbour-mail.com</span>
      </li>
    </ul>

    <p class="contact-item address">
      <svg viewBox="0 0 24 24" aria-hidden="true"><path d="M12 2a7 7 0 0 0-7 7c0 5.2 7 13 7 13s7-7.8 7-13a7 7 0 0 0-7-7zm0 9.5A2.5 2.5 0 1 1 12 6.5a2.5 2.5 0 0 1 0 5z"/></svg>
      <span>482 Halden Ave, New York, NY 10160, USA</span>
    </p>
  </section>

</main>
</body>
</html>
```